Creating a website for a life changing company (Past Q)

We do need a website for our Coaching and Consulting business we recently launched. We do need it for information purposes and that our clients do have the opportunity to subscribe for packages, programs etc.
We would like to see designs which use the colours blue and yellow (see attachment). The final design should communicate our passion for the potential in people and the benefit (going beyond) for them.
Additional information:
Our company (webpage): Past Q (the C stands for "what people cannot see / imagine now...)
Welcome to Past Q(uarter)
Consulting (R.I.M.) & Coaching (Rise further)
Two pillars:
1) R.I.M. ( Stewardship ascent - Our program - focussing on companies - business orientated)
2) Rise further (Path renewal - Events - focusing on individuals - primarily life changing)
For both of them we offer: Concierge & Past Q+ (This should go as a subscription)
Eventually you can draft this as a rhombus
Industry/Entity Type
Coaching / Consulting
Coding
Coded - Design and coding required
Number of Pages Required
1 page
Font styles to use
Other font styles liked:
- Lato
Requirements
Must have
- Please see attachment (About us / Offers / Calendar function / Links to Instagram and LinkedIn account / mailing list / page for clients
Nice to have
- A banner

```html
<!DOCTYPE html>
<html lang="en">
<head>
<meta charset="utf-8">
<title>Past Q — Coaching &amp; Consulting</title>
<link href="https://fonts.googleapis.com/css2?family=Poppins:wght@400;500;600;700&family=Roboto:wght@300;400;500;700&display=swap" rel="stylesheet">
<style>
:root{
  --navy:#062e52;
  --navy-soft:#2c4f72;
  --yellow:#f4c623;
  --ink:#1b2b3d;
  --muted:#6b7582;
  --pale:#eef5fc;
  --white:#ffffff;
  --line:#e3e8ee;
}
*{box-sizing:border-box;margin:0;padding:0}
html,body{width:1200px;height:5347px;overflow:hidden}
body{font-family:'Roboto',Arial,sans-serif;color:var(--ink);background:var(--white);position:relative}
.heading{font-family:'Poppins',Arial,sans-serif}
.abs{position:absolute}
.bar{width:40px;height:5px;background:var(--yellow);border-radius:3px;position:absolute;left:50%;margin-left:-20px}
.center{text-align:center;left:0;right:0}

/* header */
.site-header{position:absolute;top:0;left:0;width:1200px;height:129px;background:var(--white)}
.brand{position:absolute;left:85px;top:40px;height:48px;display:flex;align-items:center;gap:18px}
.brand .dash{width:24px;height:2px;background:var(--navy)}
.brand .name{font-family:'Poppins',sans-serif;font-weight:600;font-size:17px;letter-spacing:4px;color:var(--navy);width:150px;text-align:center}
.nav{position:absolute;left:365px;top:54px;display:flex;gap:22px;font-size:13px;font-weight:500;color:var(--navy)}
.nav a{color:inherit;text-decoration:none;position:relative}
.nav a.active::before{content:"";position:absolute;left:50%;top:-13px;width:6px;height:6px;background:var(--navy);margin-left:-3px}
.btn{display:inline-flex;align-items:center;justify-content:center;gap:10px;background:var(--navy);color:var(--white);border-radius:24px;font-size:13px;font-weight:500;text-decoration:none}
.btn svg{width:18px;height:10px}
.header-cta{position:absolute;left:972px;top:41px;width:143px;height:46px}

/* hero */
.hero{position:absolute;top:129px;left:0;width:1200px;height:701px;overflow:hidden}
.hero-photo{position:absolute;inset:0;background:linear-gradient(120deg,#7d93aa 0%,#50708f 40%,#2e4f70 75%,#4a6886 100%)}
.hero-shade{position:absolute;inset:0;background:rgba(6,46,82,.35)}
.hero-title{position:absolute;top:165px;font-size:72px;font-weight:700;color:var(--yellow);line-height:1}
.hero-sub{position:absolute;top:246px;font-size:72px;font-weight:700;color:var(--white);line-height:1}
.hero-lede{position:absolute;top:345px;left:390px;width:420px;text-align:center;color:var(--white);font-size:16px;font-weight:700;line-height:24px}
.hero-cta{position:absolute;top:415px;left:507px;width:187px;height:43px}
.hero-wave{position:absolute;left:0;bottom:0;width:1200px;height:701px}

/* about */
.photo{position:absolute;border-radius:4px}
.eyebrow{font-size:15px;font-weight:700;color:var(--navy)}
.about-title{position:absolute;left:644px;top:1036px;padding-left:16px;border-left:5px solid var(--yellow);font-size:38px;color:var(--navy);font-weight:300;line-height:44px}
.about-title b{font-weight:600}
.about-lead{position:absolute;left:644px;top:1106px;width:460px;font-size:16px;font-weight:700;color:var(--navy);line-height:24px}
.about-body{position:absolute;left:644px;top:1166px;width:460px;font-size:16px;color:var(--muted);line-height:24.5px}
.about-link{position:absolute;left:644px;top:1288px;font-size:13px;font-weight:500;color:var(--navy)}
.about-link u{text-underline-offset:2px}

/* ace */
.ace{position:absolute;top:1480px;left:0;width:1200px;height:633px;background:var(--pale)}
.section-title{font-size:37px;font-weight:600;color:var(--navy)}
.ace-card{position:absolute;top:231px;width:326px;height:297px;border-radius:6px;overflow:hidden;box-shadow:0 4px 14px rgba(6,46,82,.12)}
.ace-card .img{position:absolute;inset:0}
.ace-card .cap{position:absolute;left:0;right:0;bottom:0;height:90px;background:rgba(60,92,128,.78);color:var(--white);text-align:center;padding-top:22px}
.ace-card .cap h3{font-family:'Poppins',sans-serif;font-weight:600;font-size:19px}
.ace-card .cap p{font-size:14px;margin-top:2px}

/* concierge */
.service{position:absolute;top:2360px;width:320px;text-align:center}
.service svg{width:90px;height:72px}
.service h3{font-family:'Poppins',sans-serif;font-size:19px;font-weight:600;color:var(--navy);margin-top:30px}
.service p{font-size:13px;color:var(--muted);line-height:21px;margin-top:20px}

/* rise further */
.rise{position:absolute;top:2640px;left:0;width:1200px;height:883px;background:var(--navy);overflow:hidden}
.rise-card{position:absolute;top:339px;width:326px;height:440px;background:var(--white);border-radius:4px;overflow:hidden;text-align:center}
.rise-card .img{height:266px}
.rise-card h3{font-family:'Poppins',sans-serif;font-size:19px;font-weight:600;color:var(--navy);line-height:24px;margin-top:22px}
.rise-card p{font-size:13px;color:var(--muted);line-height:21px;margin:14px 38px 0}

/* plus */
.diamond-wrap{position:absolute;top:3716px;width:254px;height:254px}
.diamond{position:absolute;left:38px;top:38px;width:178px;height:178px;transform:rotate(45deg);box-shadow:0 6px 16px rgba(0,0,0,.18)}
.plus-text{position:absolute;top:3985px;width:320px;text-align:center}
.plus-text h3{font-family:'Poppins',sans-serif;font-size:19px;font-weight:600;color:var(--navy)}
.plus-text p{font-size:13px;color:var(--muted);line-height:21px;margin-top:12px}

/* newsletter */
.newsletter{position:absolute;top:4177px;left:0;width:1200px;height:266px;background:var(--pale)}
.news-title{position:absolute;left:85px;top:127px;padding-left:22px;border-left:5px solid var(--yellow);font-family:'Poppins',sans-serif;font-size:35px;line-height:42px;color:var(--navy);font-weight:400}
.news-title b{font-weight:600}
.news-form{position:absolute;left:700px;top:126px;width:415px;height:63px;border:2px solid var(--navy);border-radius:32px;background:var(--white)}
.news-form span{position:absolute;left:26px;top:21px;font-size:13px;color:#9aa3ad}
.news-form .btn{position:absolute;right:4px;top:4px;width:130px;height:51px}

/* testimonials */
.testi-title{position:absolute;left:85px;top:4548px;padding-left:20px;border-left:5px solid var(--yellow);font-family:'Poppins',sans-serif;font-size:37px;font-weight:600;color:var(--navy);line-height:44px}
.arrow-prev{position:absolute;left:1033px;top:4557px;width:26px;height:26px}
.arrow-next{position:absolute;left:1076px;top:4551px;width:38px;height:38px;border-radius:50%;background:var(--navy);display:flex;align-items:center;justify-content:center}
.quote{position:absolute;top:4619px;width:501px;height:218px;background:var(--white);box-shadow:0 4px 18px rgba(6,46,82,.1);padding:40px 38px}
.quote p{font-size:13px;color:var(--muted);line-height:21px}
.person{display:flex;align-items:center;gap:20px;margin-top:32px}
.avatar{width:50px;height:50px;border-radius:50%;background:var(--white);box-shadow:0 2px 10px rgba(0,0,0,.15);display:flex;align-items:center;justify-content:center}
.person b{display:block;font-family:'Poppins',sans-serif;font-size:17px;font-weight:500;color:var(--ink)}
.person small{font-size:13px;color:var(--navy)}

/* footer */
.site-footer{position:absolute;top:4941px;left:0;width:1200px;height:406px;background:var(--navy);color:var(--white)}
.footer-brand{position:absolute;left:492px;top:72px;width:218px;height:90px;background:var(--white);display:flex;align-items:center;justify-content:center;font-family:'Poppins',sans-serif;font-weight:600;font-size:17px;letter-spacing:4px;color:var(--navy)}
.footer-rule{position:absolute;left:85px;top:193px;width:1030px;height:1px;background:rgba(255,255,255,.35)}
.footer-nav{position:absolute;top:213px;left:0;right:0;display:flex;justify-content:center;gap:22px;font-size:13px;font-weight:500}
.copyright{position:absolute;top:271px;left:0;right:0;text-align:center;font-size:13px;font-weight:500}
.social{position:absolute;top:315px;left:0;right:0;display:flex;justify-content:center;gap:14px}
.social span{width:46px;height:46px;border-radius:50%;background:var(--white);display:flex;align-items:center;justify-content:center}
</style>
</head>
<body>

<header class="site-header">
  <div class="brand"><span class="dash"></span><span class="name">PAST Q</span><span class="dash"></span></div>
  <nav class="nav">
    <a class="active" href="#">Past Q</a><a href="#">About Us</a><a href="#">R.I.M.</a><a href="#">Concierge</a><a href="#">Rise Further</a><a href="#">Past Q +</a><a href="#">Testimonials</a>
  </nav>
  <a class="btn header-cta" href="#">Consulting <svg viewBox="0 0 18 10"><path d="M0 5h16M12 1l4 4-4 4" fill="none" stroke="#fff" stroke-width="1.4"/></svg></a>
</header>

<section class="hero">
  <div class="hero-photo" role="img" aria-label="Photo of a smiling coach presenting at a flip chart to a team in a bright meeting room"></div>
  <div class="hero-shade"></div>
  <h1 class="hero-title heading abs center" style="text-align:center">Past Q</h1>
  <p class="hero-sub heading abs center" style="text-align:center">We R.I.M. Your Company</p>
  <p class="hero-lede">We ignite the Passion in People to unleash their full Potential!</p>
  <a class="btn hero-cta" href="#">Book Your Session <svg viewBox="0 0 18 10"><path d="M0 5h16M12 1l4 4-4 4" fill="none" stroke="#fff" stroke-width="1.4"/></svg></a>
  <svg class="hero-wave" viewBox="0 0 1200 701" preserveAspectRatio="none"><path d="M0 612 C240 520 420 700 700 700 C900 700 1030 610 1200 560 L1200 701 L0 701Z" fill="#fff"/></svg>
</section>

<section class="about">
  <div class="photo" style="left:85px;top:936px;width:239px;height:362px;background:linear-gradient(160deg,#3b5f8c,#a6bccd 55%,#e8eef3)" role="img" aria-label="Portrait of a smiling coach in a navy suit"></div>
  <div class="photo" style="left:349px;top:1015px;width:239px;height:361px;background:linear-gradient(170deg,#2f8b90,#6f9a7e 45%,#2f3a48)" role="img" aria-label="Portrait of a smiling coach holding a teal umbrella outdoors"></div>
  <p class="eyebrow abs" style="left:644px;top:1005px">About Us</p>
  <h2 class="about-title heading">Welcome to <b>Past Q</b></h2>
  <p class="about-lead">Welcome to Past Q, where Passion for igniting People's Potential is in our DNA and brought Us together.</p>
  <p class="about-body">The journey starts in the Himalayas to Everest Base Camp, where transformation happened for both of them, it was going Past (Q) what they could see, comprehend and imagine.</p>
  <p class="about-link">Learn more about Lena and Marek <u>(click on image)</u></p>
</section>

<section class="ace">
  <p class="eyebrow abs center" style="top:101px;text-align:center;font-weight:500">R.I.M.</p>
  <h2 class="section-title heading abs center" style="top:130px;text-align:center">Architecture | Courage | Essentials</h2>
  <span class="bar" style="top:199px"></span>
  <div class="ace-card" style="left:85px"><div class="img" role="img" aria-label="Photo of a businessman with a briefcase gazing at a misty skyline" style="background:linear-gradient(180deg,#c7d1da,#8fa0b1 60%,#44566a)"></div><div class="cap"><h3>Architecture/adventurer</h3><p>Inspiring Exploration</p></div></div>
  <div class="ace-card" style="left:438px"><div class="img" role="img" aria-label="Photo of silhouetted climbers helping each other up a rock" style="background:linear-gradient(180deg,#7d98a6,#b5c6cc 55%,#3a4a52)"></div><div class="cap"><h3>Courage</h3><p>Culture Of Courage</p></div></div>
  <div class="ace-card" style="left:789px"><div class="img" role="img" aria-label="Photo of a hiker with a backpack overlooking a hazy valley" style="background:linear-gradient(180deg,#b7c1cb,#8795a4 60%,#556779)"></div><div class="cap"><h3>Essentials / Evaluation</h3><p>Understanding Your WHY</p></div></div>
</section>

<section class="concierge">
  <h2 class="section-title heading abs center" style="top:2208px;text-align:center">Concierge</h2>
  <span class="bar" style="top:2265px"></span>
  <p class="abs center" style="top:2290px;text-align:center;font-size:16px;font-weight:500;color:var(--muted);line-height:25px">Concierge Package offers you an ongoing partnership as you navigate your<br>journey to reach your full potential.</p>
  <div class="service" style="left:87px">
    <svg viewBox="0 0 90 72"><circle cx="26" cy="38" r="18" fill="#d5dbe1"/><rect x="32" y="8" width="26" height="22" fill="none" stroke="#062e52" stroke-width="2" stroke-dasharray="3 3"/><circle cx="38" cy="40" r="8" fill="none" stroke="#062e52" stroke-width="2"/><path d="M34 50v14h8V50" fill="none" stroke="#062e52" stroke-width="2"/><circle cx="66" cy="44" r="8" fill="none" stroke="#062e52" stroke-width="2"/><path d="M58 64l8-12 8 12" fill="none" stroke="#062e52" stroke-width="2"/></svg>
    <h3>Coaching</h3>
    <p>Concierge Package offers you an ongoing partnership as you navigate your journey to reach your full potential.</p>
  </div>
  <div class="service" style="left:440px">
    <svg viewBox="0 0 90 72"><circle cx="26" cy="38" r="18" fill="#d5dbe1"/><rect x="30" y="10" width="40" height="26" rx="3" fill="none" stroke="#062e52" stroke-width="2"/><path d="M38 20h24M38 27h16" stroke="#062e52" stroke-width="2"/><circle cx="42" cy="48" r="6" fill="none" stroke="#062e52" stroke-width="2"/><circle cx="60" cy="48" r="6" fill="none" stroke="#062e52" stroke-width="2"/><path d="M34 66c0-7 16-7 16 0M52 66c0-7 16-7 16 0" fill="none" stroke="#062e52" stroke-width="2"/></svg>
    <h3>Consulting</h3>
    <p>Concierge Package offers you an ongoing partnership as you navigate your journey to reach your full potential.</p>
  </div>
  <div class="service" style="left:791px">
    <svg viewBox="0 0 90 72"><circle cx="26" cy="38" r="18" fill="#d5dbe1"/><path d="M32 14h38a8 8 0 0 1 8 8v18a8 8 0 0 1-8 8H52l-10 10v-10h-10a8 8 0 0 1-8-8V22a8 8 0 0 1 8-8z" fill="none" stroke="#062e52" stroke-width="2"/><circle cx="42" cy="31" r="2.5" fill="#062e52"/><circle cx="51" cy="31" r="2.5" fill="#062e52"/><circle cx="60" cy="31" r="2.5" fill="#062e52"/></svg>
    <h3>Fireside Chat</h3>
    <p>Concierge Package offers you an ongoing partnership as you navigate your journey to reach your full potential.</p>
  </div>
</section>

<section class="rise">
  <svg class="abs" style="left:0;top:0" width="1200" height="140" viewBox="0 0 1200 140" preserveAspectRatio="none"><path d="M0 0H1200V24C1080 10 1000 30 900 70C760 128 600 126 420 110C240 94 100 90 0 122Z" fill="#fff"/></svg>
  <h2 class="section-title heading abs center" style="top:220px;text-align:center;color:#fff">Rise Further</h2>
  <span class="bar" style="top:293px"></span>
  <article class="rise-card" style="left:85px"><div class="img" role="img" aria-label="Photo of a hiker with a yellow jacket and backpack walking into a forest" style="background:linear-gradient(180deg,#5c6a55,#8a6b3c 60%,#3b3a30)"></div><h3>Rise Further Light<br>(Half day)</h3><p>This is a fantastic opportunity to understand. WHY you carry the heavy backpack throughout your life.</p></article>
  <article class="rise-card" style="left:437px"><div class="img" role="img" aria-label="Photo of hands unpacking items from an open case" style="background:linear-gradient(160deg,#c9c2b8,#8b8783 55%,#4d5160)"></div><h3>Rise Further<br>(2–3 days)</h3><p>We invite you to unpack your backpack, inspect the items you are carrying and decide WHAT to carry.</p></article>
  <article class="rise-card" style="left:789px"><div class="img" role="img" aria-label="Photo of a hiker leaping joyfully with a backpack by a lake" style="background:linear-gradient(180deg,#b8c1c6,#8c9aa0 55%,#56704c)"></div><h3>Rise Further Unlimited<br>(1 week)</h3><p>You design your new backpack and decide HOW you want to carry it through your life.</p></article>
</section>

<section class="plus">
  <h2 class="section-title heading abs center" style="top:3616px;text-align:center">Past Q+</h2>
  <span class="bar" style="top:3680px"></span>
  <div class="diamond-wrap" style="left:124px"><div class="diamond" role="img" aria-label="Photo of a smiling woman sitting on a sofa with a laptop" style="background:linear-gradient(135deg,#c9c5c0,#e7c46a 50%,#5a6d84)"></div></div>
  <div class="diamond-wrap" style="left:474px"><div class="diamond" role="img" aria-label="Photo of a hand reaching out against a dark blue background" style="background:linear-gradient(135deg,#0d3760,#d8a98a 55%,#0d3760)"></div></div>
  <div class="diamond-wrap" style="left:825px"><div class="diamond" role="img" aria-label="Word collage about business resources in red and grey" style="background:linear-gradient(135deg,#d9d9d9,#c43a2f 50%,#8d8d8d)"></div></div>
  <div class="plus-text" style="left:91px"><h3>Coaching Insights</h3><p>Become familiar with the insights and principles of coaching and understand their benefits.</p></div>
  <div class="plus-text" style="left:441px"><h3>Grab and go</h3><p>Invitation to grab valuable tips to make a change in your life!</p></div>
  <div class="plus-text" style="left:792px"><h3>Be Resourceful</h3><p>Pay attention to the valuable resources which you could benefit from.</p></div>
</section>

<section class="newsletter">
  <p class="eyebrow abs" style="left:85px;top:78px">Subscribe Newsletter</p>
  <h2 class="news-title">Subscribe for <b>packages</b><br><b>&amp; programs</b></h2>
  <div class="news-form"><span>Enter email</span><a class="btn" href="#">Subscribe <svg viewBox="0 0 18 10"><path d="M0 5h16M12 1l4 4-4 4" fill="none" stroke="#fff" stroke-width="1.4"/></svg></a></div>
</section>

<section class="testimonials">
  <h2 class="testi-title">Testimonials</h2>
  <svg class="arrow-prev" viewBox="0 0 26 26"><path d="M24 13H3M9 7l-6 6 6 6" fill="none" stroke="#062e52" stroke-width="1.6"/></svg>
  <span class="arrow-next"><svg width="20" height="12" viewBox="0 0 20 12"><path d="M0 6h18M13 1l5 5-5 5" fill="none" stroke="#fff" stroke-width="1.6"/></svg></span>
  <article class="quote" style="left:85px">
    <p>Facilisis vestibulum aliquet vulputate ut pretium. Class luctus torquent amet bibendum quisque himenaeos. Parturient malesuada dui accumsan montes tempor augue curae amet per.</p>
    <div class="person"><span class="avatar"><svg width="20" height="22" viewBox="0 0 20 22"><circle cx="10" cy="6" r="5" fill="#1b2b3d"/><path d="M1 22c0-7 18-7 18 0z" fill="#1b2b3d"/></svg></span><div><b>Clara Dunmore</b><small>United States</small></div></div>
  </article>
  <article class="quote" style="left:614px">
    <p>Facilisis vestibulum aliquet vulputate ut pretium. Class luctus torquent amet bibendum quisque himenaeos. Parturient malesuada dui accumsan montes tempor augue curae amet per.</p>
    <div class="person"><span class="avatar"><svg width="20" height="22" viewBox="0 0 20 22"><circle cx="10" cy="6" r="5" fill="#1b2b3d"/><path d="M1 22c0-7 18-7 18 0z" fill="#1b2b3d"/></svg></span><div><b>Clara Dunmore</b><small>United States</small></div></div>
  </article>
</section>

<footer class="site-footer">
  <div class="footer-brand">PAST Q</div>
  <div class="footer-rule"></div>
  <nav class="footer-nav"><span>Past Q</span><span>About Us</span><span>R.I.M.</span><span>Concierge</span><span>Rise Further</span><span>Past Q +</span><span>Testimonials</span></nav>
  <p class="copyright">Copyright © 2022 Past Q, All rights reserved.</p>
  <div class="social">
    <span aria-label="Email"><svg width="20" height="14" viewBox="0 0 20 14"><rect width="20" height="14" rx="2" fill="#062e52"/><path d="M1 1l9 7 9-7" fill="none" stroke="#fff" stroke-width="1.4"/></svg></span>
    <span aria-label="Social profile"></span>
  </div>
</footer>

</body>
</html>
```